Real Estate Card Design

I need a new business card! Below you will find my headshot, the company logo and a copy of my previous business card.

The card must contain the following information:

Dana Welch
Sales Representative
FAIR HARBOUR HOMES REALTY INC BROKERGE
204-517 Maple Ave E, Oshawa ON L1G 4K7
Cell: 905-618-4037 Office:905-481-2696
www.danawelch.com dana@movewithwelch.ca

I would like the card to portray security and class all the while being fresh and contemporary. I hold the key....

```html
<!DOCTYPE html>
<html lang="en">
<head>
<meta charset="utf-8">
<title>Dana Welch – Business Card</title>
<link href="https://fonts.googleapis.com/css2?family=Ubuntu:wght@400;500;700&family=Tinos:wght@400&family=Fira+Sans+Condensed:wght@500;600&display=swap" rel="stylesheet">
<style>
  :root {
    --page-bg: #f2f2f2;
    --card-white: #ffffff;
    --card-black: #000000;
    --accent-blue: #4cc6f4;
    --accent-deep: #1a6fb8;
    --ink-dark: #1a1a1a;
    --text-light: #ffffff;
    --photo-teal: #1c4a5a;
    --photo-dark: #05141a;
  }
  * { margin: 0; padding: 0; box-sizing: border-box; }
  html, body {
    width: 1200px; height: 1200px; overflow: hidden;
    background: var(--page-bg);
  }
  .card {
    position: absolute; left: 80px; top: 285px;
    width: 1040px; height: 630px;
    background: var(--card-black);
    box-shadow: 0 2px 10px rgba(0,0,0,0.18);
    overflow: hidden;
  }
  .card-top {
    position: absolute; left: 0; top: 0; width: 100%; height: 200px;
    background: var(--card-white);
  }
  .divider {
    position: absolute; left: 0; top: 200px; width: 100%; height: 6px;
    background: linear-gradient(90deg, var(--accent-deep), var(--accent-blue) 35%, #1b3a4d 75%, #0d1a22);
  }
  .brand {
    position: absolute; left: 60px; top: 29px; width: 300px;
    display: flex; flex-direction: column; align-items: center;
  }
  .brand-square {
    width: 125px; height: 100px; background: var(--accent-blue);
  }
  .brand-name {
    margin-top: 10px;
    font-family: "Tinos", serif; font-size: 30px; color: var(--ink-dark);
    letter-spacing: 0.5px; white-space: nowrap;
  }
  .agent {
    position: absolute; right: 52px; top: 36px; text-align: right;
    font-family: "Ubuntu", sans-serif;
  }
  .agent-name { font-size: 45px; font-weight: 500; color: var(--accent-blue); line-height: 1.15; }
  .agent-title { font-size: 32px; color: var(--ink-dark); line-height: 1.3; }
  .agent-cell { font-size: 37px; color: var(--ink-dark); line-height: 1.3; }
  .company {
    position: absolute; left: 48px; top: 240px;
    font-family: "Tinos", serif; font-size: 41px; color: var(--text-light);
    line-height: 48px; letter-spacing: 1px;
  }
  .contacts {
    position: absolute; left: 42px; top: 408px;
    font-family: "Fira Sans Condensed", sans-serif; font-weight: 600;
    font-size: 33px; color: var(--text-light); line-height: 48.5px;
    list-style: none;
  }
  .portrait-glow {
    position: absolute; right: 0; top: 206px; width: 520px; height: 424px;
    background: radial-gradient(ellipse at 75% 55%, var(--photo-teal) 0%, #0f2a35 40%, rgba(0,0,0,0) 75%);
  }
  .portrait {
    position: absolute; right: 0; top: 270px; width: 300px; height: 360px;
    background: linear-gradient(180deg, #8b7a62 0%, #2a2a30 45%, #111418 100%);
    border-radius: 140px 140px 0 0;
  }
</style>
</head>
<body>
  <div class="card">
    <div class="card-top"></div>
    <div class="divider"></div>

    <div class="brand">
      <div class="brand-square"></div>
      <div class="brand-name">FAIR HARBOUR HOMES</div>
    </div>

    <div class="agent">
      <div class="agent-name">Dana Welch</div>
      <div class="agent-title">SALES REPRESENTATIVE</div>
      <div class="agent-cell">Cell: 905-618-4037</div>
    </div>

    <div class="company">FAIR HARBOUR HOMES<br>REALTY INC BROKERGE</div>

    <ul class="contacts">
      <li>Office: 905-481-2696</li>
      <li>www.danawelch.com</li>
      <li>dana@movewithwelch.ca</li>
      <li>204-517 Maple Ave E, Oshawa ON L1G 4K7</li>
    </ul>

    <div class="portrait-glow"></div>
    <div class="portrait" role="img" aria-label="Headshot of Dana Welch in a dark pinstripe suit holding up a house key"></div>
  </div>
</body>
</html>
```